Tamarind Crest Management - Business Cards

I need business cards. My current logo was designed by a designer at this site and I very much like and am happy with the results. I would like a business card that is trendy, unique, current yet professional. I deal with high net worth clients daily

Target Market(s)

Out of state investors looking to get into the rental market in Ohio

Industry/Entity Type

Property Management, Consulting

Contact Information for Business Card

Name, Title (Chief Financial Officer) office phone number (347) 681-9072 website address tamcrestmgmt.example

Font styles to use
Sans Serif

Colors
0054AA
0677BA
7BADD7
CADEEF
E8F1F8
0094D4
00A9DD
6FCCEA
C7EBF8
E9F6FB
00AB8E
00BBA5
67D7C9
C6EFE9
E9F9F6

```html
<!DOCTYPE html>
<html lang="en">
<head>
<meta charset="utf-8">
<title>Tamarind Crest Management – Business Card</title>
<link rel="stylesheet" href="https://fonts.googleapis.com/css2?family=Montserrat:wght@400;500;700&display=swap">
<style>
  :root {
    --page-bg: #e4ddd3;
    --card-bg: #efebe5;
    --card-edge: #f7f5f1;
    --navy: #1f2d4d;
    --ink: #2a2a2e;
    --ink-soft: #35353a;
    --accent-red: #c8343a;
  }
  * { box-sizing: border-box; margin: 0; padding: 0; }
  html, body {
    width: 1200px;
    height: 1047px;
    overflow: hidden;
    background: var(--page-bg);
    font-family: "Montserrat", Arial, sans-serif;
  }
  .card {
    position: absolute;
    left: 125px;
    top: 264px;
    width: 950px;
    height: 520px;
    border-radius: 26px;
    background: var(--card-bg);
    border: 2px solid var(--card-edge);
  }
  .brand {
    position: absolute;
    left: 70px;
    top: 190px;
    width: 230px;
    display: flex;
    align-items: center;
    gap: 12px;
  }
  .brand-mark {
    flex: none;
    width: 18px;
    height: 18px;
    background: var(--navy);
  }
  .brand-name {
    font-weight: 700;
    font-size: 25px;
    line-height: 1.15;
    color: var(--navy);
    text-transform: uppercase;
  }
  .divider {
    position: absolute;
    left: 330px;
    top: 150px;
    width: 3px;
    height: 220px;
    background: var(--navy);
  }
  .details {
    position: absolute;
    left: 385px;
    top: 162px;
  }
  .person-name {
    font-weight: 700;
    font-size: 39px;
    letter-spacing: 0.5px;
    color: var(--navy);
    line-height: 1;
  }
  .person-title {
    margin-top: 14px;
    font-weight: 500;
    font-size: 22px;
    color: var(--ink-soft);
  }
  .contacts {
    list-style: none;
    margin-top: 38px;
  }
  .contact {
    display: flex;
    align-items: center;
    gap: 10px;
    font-weight: 500;
    font-size: 22px;
    color: var(--ink);
    height: 38px;
  }
  .contact svg {
    width: 20px;
    height: 20px;
    fill: var(--ink);
    flex: none;
  }
</style>
</head>
<body>
  <div class="card">
    <div class="brand">
      <span class="brand-mark"></span>
      <span class="brand-name">Tamarind Crest Management</span>
    </div>
    <div class="divider"></div>
    <div class="details">
      <h1 class="person-name">DANA MORROW</h1>
      <p class="person-title">Chief Financial Officer</p>
      <ul class="contacts">
        <li class="contact">
          <svg viewBox="0 0 20 20" aria-hidden="true"><path d="M2 8c0-3 4-4 8-4s8 1 8 4v1h-4V7.5c-1-.5-2.5-.7-4-.7s-3 .2-4 .7V9H2z"/><path d="M5 10l2-2h6l2 2 2 6H3z"/></svg>
          (347) 681-9072
        </li>
        <li class="contact">
          <svg viewBox="0 0 20 20" aria-hidden="true"><path d="M2 5h16v1l-8 5-8-5z"/><path d="M2 8l8 5 8-5v7H2z"/></svg>
          info@tamcrestmgmt.example
        </li>
        <li class="contact">
          <svg viewBox="0 0 20 20" aria-hidden="true"><circle cx="10" cy="10" r="8"/><path d="M5 6c2 0 3 1 3 2s-2 1-2 3 2 2 2 4M13 4c-1 1 0 2 1 3s2 2 2 4" stroke="#efebe5" stroke-width="1.3" fill="none"/></svg>
          tamcrestmgmt.example
        </li>
      </ul>
    </div>
  </div>
</body>
</html>
```